Harbor Learning Center Posters Showing Building Blocks

We need poster designs for a School in Arizona for kids with Autism. There will be 4 such posters needed which highlight our schools building blocks. Requirements for all 4 posters are as followed: 1) We need the Harbor Learning Center Logo on each poster. I have included attachment. 2) The posters need the following titles: Building Block #1 (for the first poster), Building Block #2 for the 2nd poster, Building Block #3 for the 3rd poster, and Building Block #4 for the forth poster. 3) The main text and focus of the posters will be the following key words: For the first poster the words "Kids first in every decision". The words for the second poster are: "Students are friends with each other, and welcome new students with open arms." The words for the 3rd poster are: "The school is quiet, and students are working hard to do their best." The words for the 4th poster are: "Parents see amazing improvement in their child." 4) We would love to use some of the kids art from our schools if possible. Use your expertise to decide. I will send these out as well. 5) Try and design the posters around the key words from each poster 6) I am sure if landscape or portrait would be best so I will let the experts decide. All 4 posters need to be the same layout once decided.

Target Market(s)

These posters are for the school only. Prospective students/parents will see these posters so they will be used for Marketing from that perspective. We may put out into local community in future.

Industry/Entity Type

School

Font styles to use
Serif

Requirements
Must have
• 1) Logo (Harbor Learning Center for Growth and Discovery)
• 2) Title: as described in write up
• 3) Key words: as described in write up
Nice to have
• Kids art from school. Note: This is the first time that I have been on this site so I may have made a mistake by putting 4 posters on one project. I am assuming that I would need to pay more to have 4 posters so let me know if I need to modify the project in any way?

```html
<!DOCTYPE html>
<html lang="en">
<head>
<meta charset="utf-8">
<title>Building Block #1 – Kids first in every decision</title>
<link rel="stylesheet" href="https://fonts.googleapis.com/css2?family=Playfair+Display:wght@700;900&display=swap">
<style>
  :root {
    --paper: #ffffff;
    --ink: #1c1a1f;
    --art-green: #3f7a3a;
    --art-orange: #e2632b;
    --art-red: #c4332a;
    --art-blue: #2f5f8f;
    --art-teal: #3aa39a;
    --art-dark: #1e1b22;
    --art-yellow: #e9b33a;
    --contact: #ffffff;
    --badge-red: #c8322b;
  }
  * { margin: 0; padding: 0; box-sizing: border-box; }
  html, body { width: 857px; height: 1200px; overflow: hidden; background: var(--paper); }
  .poster {
    position: relative;
    width: 857px;
    height: 1200px;
    background: var(--paper);
    overflow: hidden;
  }
  .key-words {
    position: absolute;
    left: 40px;
    top: 14px;
    width: 800px;
    font-family: "Playfair Display", Georgia, serif;
    font-weight: 900;
    font-size: 182px;
    line-height: 166px;
    letter-spacing: -1px;
    color: transparent;
    background: linear-gradient(135deg,
      var(--art-dark) 0%, var(--art-green) 14%, var(--art-orange) 26%,
      var(--art-dark) 36%, var(--art-blue) 48%, var(--art-red) 58%,
      var(--art-teal) 68%, var(--art-dark) 78%, var(--art-orange) 88%, var(--art-green) 100%);
    -webkit-background-clip: text;
    background-clip: text;
  }
  .kids-art {
    position: absolute;
    left: 0;
    top: 700px;
    width: 857px;
    height: 500px;
    background:
      radial-gradient(ellipse at 20% 30%, rgba(226,99,43,.85), transparent 45%),
      radial-gradient(ellipse at 70% 25%, rgba(63,122,58,.85), transparent 45%),
      radial-gradient(ellipse at 45% 70%, rgba(47,95,143,.7), transparent 50%),
      radial-gradient(ellipse at 85% 75%, rgba(196,51,42,.75), transparent 45%),
      linear-gradient(160deg, var(--art-dark), var(--art-green) 40%, var(--art-orange) 70%, var(--art-dark));
  }
  .block-title {
    position: absolute;
    left: 36px;
    top: 1144px;
    font-family: "Playfair Display", Georgia, serif;
    font-weight: 700;
    font-size: 28px;
    line-height: 34px;
    color: var(--contact);
  }
  .contact {
    position: absolute;
    left: 320px;
    top: 1136px;
    width: 320px;
    font-family: "Playfair Display", Georgia, serif;
    font-weight: 700;
    font-size: 19px;
    line-height: 25px;
    color: var(--contact);
    text-align: center;
  }
  .brand {
    position: absolute;
    left: 660px;
    top: 1128px;
    width: 184px;
    height: 58px;
    background: var(--paper);
    display: flex;
    align-items: center;
    gap: 8px;
    padding: 6px 8px;
  }
  .brand-dot {
    flex: none;
    width: 22px;
    height: 22px;
    border-radius: 50%;
    background: var(--badge-red);
  }
  .brand-name {
    font-family: "Playfair Display", Georgia, serif;
    font-weight: 700;
    font-size: 11px;
    line-height: 13px;
    color: var(--badge-red);
  }
</style>
</head>
<body>
  <main class="poster">
    <h1 class="key-words">"Kids<br>first<br>in every<br>decision"</h1>
    <div class="kids-art" role="img" aria-label="Colourful children's painting with green, orange, red and blue brush strokes"></div>
    <h2 class="block-title">Building Block #1</h2>
    <p class="contact">www.harborlearningcenter.org<br>480-555-0142</p>
    <div class="brand">
      <span class="brand-dot"></span>
      <span class="brand-name">Harbor Learning Center for Growth and Discovery</span>
    </div>
  </main>
</body>
</html>
```